Company PowerPoint Presentation Template

I am looking for a business powerpoint template tailored to my company that specializes in permafrost services for the mining, transportation, and oil & gas industries. The template would be used to present project findings from studies completed for our clients. I am looking for a crisp, technical, professional business look to the template. Our business is located in North America and English is the primary language used to communicate our work. Complimentary colors associated with the business is blue (RGB, 0,112,192) or something similar in color.

```html
<!DOCTYPE html>
<html lang="en">
<head>
<meta charset="utf-8">
<title>Frostline Ground Consulting – Presentation Template</title>
<link href="https://fonts.googleapis.com/css2?family=Michroma&family=Montserrat:wght@500;700&family=Raleway:wght@400;500&display=swap" rel="stylesheet">
<style>
  :root{
    --blue:#0a6cc8;
    --blue-deep:#0d4f95;
    --blue-mid:#2d8fe0;
    --blue-light:#8cc3f2;
    --ink:#1d2b3f;
    --text:#444b55;
    --slide:#ecedef;
    --card:#f4f4f5;
    --stage-top:#c0c7ca;
    --stage-bottom:#e5e5e5;
  }
  *{box-sizing:border-box;margin:0;padding:0}
  html,body{width:737px;height:1200px;overflow:hidden}
  body{
    position:relative;
    background:linear-gradient(180deg,var(--stage-top) 0,#d3d7d8 470px,var(--stage-bottom) 490px,var(--stage-bottom) 100%);
    font-family:"Raleway",sans-serif;color:var(--text);
  }
  .slide{position:absolute;background:linear-gradient(120deg,#f3f3f4,var(--slide));overflow:hidden;box-shadow:0 8px 14px -8px rgba(0,0,0,.35)}
  .abs{position:absolute}
  .photo{position:absolute}
  .tag{position:absolute;height:11px;padding-left:4px;background:linear-gradient(90deg,var(--blue) 70%,rgba(10,108,200,0));color:#fff;font-family:"Michroma",sans-serif;font-size:7.5px;line-height:11px;letter-spacing:.3px}
  .lead{position:absolute;font-family:"Montserrat",sans-serif;font-weight:700;color:var(--ink);text-transform:uppercase}
  .body{position:absolute;font-size:5px;line-height:7.4px;color:var(--text);text-align:justify}
  .card{position:absolute;background:var(--card);box-shadow:0 2px 5px rgba(0,0,0,.2);text-align:center}
  .card-title{font-family:"Montserrat",sans-serif;font-weight:700;font-size:5.2px;color:var(--ink)}
  .card-text{font-size:4.6px;line-height:6.4px;color:var(--text)}
  .tech{font-family:"Michroma",sans-serif;color:var(--blue)}
  .icon{stroke:var(--blue);fill:none;stroke-width:1.2;stroke-linecap:round;stroke-linejoin:round}

  /* cover */
  .cover{position:absolute;left:148px;top:118px;width:440px;height:248px;background:linear-gradient(135deg,#e4e6e8,#b9bdc1 60%,#d7dadc);box-shadow:0 12px 18px -10px rgba(0,0,0,.4)}
  .cover-panel{position:absolute;left:11px;top:11px;width:418px;height:226px;background:linear-gradient(160deg,#1670c6,var(--blue) 55%,#0b5fae);clip-path:polygon(0 0,100% 0,100% 100%,9% 100%,0 84%)}
  .cover-rule{position:absolute;left:70px;width:300px;height:1px;background:rgba(255,255,255,.85)}
  .cover-name{position:absolute;left:0;width:100%;text-align:center;color:#fff;font-family:"Michroma",sans-serif}

  .brand{position:absolute;left:412px;top:1030px;width:276px;text-align:center;font-family:"Michroma",sans-serif;color:#16191d}
</style>
</head>
<body>

<!-- Cover slide -->
<section class="cover" aria-label="Cover slide">
  <div class="cover-panel" role="img" aria-label="Blue-tinted photo of an industrial pipeline facility">
    <div class="cover-rule" style="top:58px"></div>
    <div class="cover-name" style="top:70px;font-size:33px;letter-spacing:1px">FROSTLINE</div>
    <div class="cover-name" style="top:122px;font-size:10px;letter-spacing:5px">GROUND CONSULTING</div>
    <div class="cover-rule" style="top:148px"></div>
    <div class="cover-name" style="top:160px;font-size:9px;font-family:'Montserrat',sans-serif;font-weight:700">www.frostlineground.com</div>
  </div>
</section>

<!-- About us 1 -->
<section class="slide" style="left:25px;top:530px;width:343px;height:193px">
  <div class="photo" role="img" aria-label="Photo of yellow pipeline valves with handwheels" style="left:0;top:0;width:121px;height:193px;background:linear-gradient(135deg,#3b3a2c,#b99a25 35%,#6b5a1e 60%,#2a2a25)"></div>
  <div class="tag" style="left:135px;top:16px;width:80px">ABOUT US</div>
  <p class="lead" style="left:135px;top:36px;width:200px;font-size:5.7px;line-height:10.5px">Lorem ipsum is simply dummy text of the printing and typesetting industry printer took a galley.</p>
  <p class="body" style="left:135px;top:60px;width:195px">Lorem Ipsum is simply dummy text of the printing and typesetting industry. Lorem Ipsum has been the industry's standard dummy text ever make a type specimen book. It has survived not only five centuries.</p>
  <div class="card" style="left:149px;top:96px;width:80px;height:79px">
    <svg class="abs icon" style="left:30px;top:10px" width="20" height="14" viewBox="0 0 20 14"><rect x="1" y="1" width="11" height="9"/><path d="M12 4h4l3 3v3h-7z"/><circle cx="5" cy="11.5" r="1.5"/><circle cx="15" cy="11.5" r="1.5"/></svg>
    <div class="card-title abs" style="left:0;width:100%;top:37px">HEADING HERE</div>
    <p class="card-text abs" style="left:7px;width:66px;top:49px">Lorem Ipsum is simply dummy text of the printing and typesetting industry.</p>
  </div>
  <div class="card" style="left:236px;top:96px;width:80px;height:79px">
    <svg class="abs icon" style="left:32px;top:7px" width="16" height="21" viewBox="0 0 16 21"><rect x="2" y="2" width="12" height="14" rx="3"/><path d="M4 6h8v4H4zM5 1h6M4 19l2-3M12 19l-2-3"/><circle cx="5" cy="13" r=".8"/><circle cx="11" cy="13" r=".8"/></svg>
    <div class="card-title abs" style="left:0;width:100%;top:37px">HEADING HERE</div>
    <p class="card-text abs" style="left:7px;width:66px;top:49px">Lorem Ipsum is simply dummy text of the printing and typesetting industry.</p>
  </div>
</section>

<!-- About us 2 -->
<section class="slide" style="left:379px;top:530px;width:342px;height:193px">
  <div class="tag" style="left:30px;top:22px;width:80px;background:var(--blue);clip-path:polygon(0 0,100% 0,93% 100%,0 100%)">ABOUT US</div>
  <p class="lead" style="left:30px;top:40px;width:170px;font-size:10px;line-height:12.5px">Lorem ipsum is simply typesetting industry</p>
  <p class="body" style="left:31px;top:74px;width:153px">Lorem Ipsum is simply dummy text of the printing and typesetting industry. Lorem Ipsum has been the industry's standard dummy text ever make a only five centuries.</p>
  <div class="photo" role="img" aria-label="Photo of pipelines at sunset with industrial smoke" style="left:214px;top:0;width:128px;height:193px;background:linear-gradient(180deg,#6b5a4a,#d58c33 40%,#f2b24c 55%,#6a4a2c 80%,#3a2c22)"></div>
  <div class="photo" role="img" aria-label="Photo of stacked blue barrels" style="left:0;top:125px;width:119px;height:68px;background:radial-gradient(circle at 30% 40%,#3b8fda,#13508f 60%,#0c2f55)"></div>
  <div class="abs" style="left:119px;top:125px;width:95px;height:68px;background:var(--blue)">
    <svg class="abs" style="left:30px;top:9px;stroke:#fff;fill:none;stroke-width:1.2" width="22" height="12" viewBox="0 0 22 12"><rect x="1" y="1" width="13" height="7"/><path d="M14 3h4l3 3v2h-7z"/><circle cx="5" cy="10" r="1.3"/><circle cx="17" cy="10" r="1.3"/></svg>
    <div class="abs" style="left:8px;top:28px;color:#fff;font-family:'Montserrat',sans-serif;font-weight:700;font-size:5.5px">HEADING</div>
    <p class="abs" style="left:8px;top:37px;width:80px;color:#fff;font-size:3.3px;line-height:4.6px">Lorem Ipsum is simply dummy text of the printing and typesetting industry. Lorem Ipsum has been the industry's standard dummy text ever make a only five centuries.</p>
  </div>
</section>

<!-- Our graph -->
<section class="slide" style="left:27px;top:736px;width:342px;height:193px">
  <div class="abs" style="left:0;top:0;width:52px;height:193px;background:var(--blue)"></div>
  <div class="photo" role="img" aria-label="Photo of pipelines running toward a hazy sunset" style="left:9px;top:10px;width:100px;height:173px;background:linear-gradient(180deg,#d8c98a,#c5b36a 40%,#5c5a48 60%,#2c2e2c)"></div>
  <div class="tag" style="left:114px;top:20px;width:125px;height:16px;font-size:11px;line-height:16px">OUR GRAPH</div>
  <p class="body" style="left:114px;top:47px;width:180px;font-size:2.9px;line-height:4px">Lorem Ipsum is simply dummy text of the printing and typesetting industry. Lorem Ipsum has been the industry's standard dummy text ever since the 1500s, when an unknown printer took a galley of type and scrambled it to make a type specimen book. It has survived not only five centuries, but also the leap into electronic typesetting, remaining.</p>
  <div class="card" style="left:114px;top:105px;width:69px;height:78px">
    <svg class="abs" style="left:14px;top:4px" width="40" height="40" viewBox="0 0 40 40"><circle cx="20" cy="20" r="17" fill="none" stroke="#cfd3d8" stroke-width="1"/><circle cx="20" cy="20" r="17" fill="none" stroke="var(--blue)" stroke-width="2" stroke-dasharray="32 107" transform="rotate(-90 20 20)"/><text x="20" y="23" text-anchor="middle" font-family="Michroma,sans-serif" font-size="7.5" fill="var(--blue)">30%</text></svg>
    <p class="card-text abs" style="left:12px;width:45px;top:46px;font-size:3.4px;line-height:4.6px">Lorem Ipsum is make a simply dummy text only five centuries.</p>
    <svg class="abs icon" style="left:29px;top:62px" width="11" height="13" viewBox="0 0 11 13"><rect x="1" y="1" width="9" height="9" rx="2"/><path d="M2.5 3.5h6v3h-6zM2 12l1.5-2M9 12l-1.5-2"/></svg>
  </div>
  <div class="card" style="left:192px;top:105px;width:69px;height:78px;background:#fff">
    <svg class="abs" style="left:14px;top:4px" width="40" height="40" viewBox="0 0 40 40"><circle cx="20" cy="20" r="17" fill="none" stroke="#e2e4e7" stroke-width="1"/><circle cx="20" cy="20" r="17" fill="none" stroke="var(--blue)" stroke-width="2" stroke-dasharray="74 107" transform="rotate(-90 20 20)"/><text x="20" y="22" text-anchor="middle" font-family="Michroma,sans-serif" font-size="7.5" fill="var(--blue)">40%</text></svg>
    <p class="card-text abs" style="left:12px;width:45px;top:46px;font-size:3.4px;line-height:4.6px">Lorem Ipsum is make a simply dummy text only five centuries.</p>
    <svg class="abs icon" style="left:28px;top:62px" width="13" height="12" viewBox="0 0 13 12"><rect x="1" y="2" width="11" height="9" rx="1"/><path d="M3 7l1.5-3h4L10 7zM1 1h11"/></svg>
  </div>
  <div class="card" style="left:266px;top:105px;width:70px;height:78px;background:#fff;text-align:left">
    <div class="tech abs" style="left:4px;top:8px;font-size:7.5px;font-style:normal">70%</div>
    <div class="tech abs" style="left:4px;top:22px;font-size:5.2px">HEADING HERE</div>
    <p class="card-text abs" style="left:4px;top:32px;width:58px;font-size:3.3px;line-height:4.4px;text-align:justify">Lorem Ipsum is simply dummy text of the printing and typesetting industry. Lorem with the release of Letraset sheets</p>
  </div>
</section>

<!-- Chart slide -->
<section class="slide" style="left:378px;top:736px;width:339px;height:191px">
  <div class="abs" style="left:0;top:0;width:96px;height:191px;background:var(--blue)"></div>
  <div class="card" style="left:22px;top:22px;width:106px;height:143px;background:#eceef0">
    <div class="abs" style="left:0;width:100%;top:10px;font-family:'Michroma',sans-serif;font-size:7.5px;color:var(--ink)">HEADING HERE</div>
    <svg class="abs" style="left:10px;top:27px" width="86" height="86" viewBox="0 0 86 86">
      <g fill="none" stroke-width="22" transform="rotate(-110 43 43)">
        <circle cx="43" cy="43" r="32" stroke="var(--blue-deep)" stroke-dasharray="201 201"/>
        <circle cx="43" cy="43" r="32" stroke="#1567c4" stroke-dasharray="50 201"/>
        <circle cx="43" cy="43" r="32" stroke="var(--blue-mid)" stroke-dasharray="0 50 50 201"/>
        <circle cx="43" cy="43" r="32" stroke="var(--blue-light)" stroke-dasharray="0 150 51 201"/>
      </g>
      <g font-family="Michroma,sans-serif" font-size="5.5" fill="#fff" text-anchor="middle">
        <text x="53" y="18">50%</text><text x="74" y="49">30%</text><text x="35" y="72">90%</text><text x="11" y="35">30%</text>
      </g>
    </svg>
    <p class="abs" style="left:8px;width:90px;top:124px;font-size:3.8px;line-height:5.2px;color:var(--blue)">Lorem Ipsum is simply dummy text of the printing and typesetting industry.</p>
  </div>
  <div class="abs" style="left:176px;top:33px;width:140px">
    <div style="position:relative;height:33px">
      <div class="abs tech" style="left:0;top:0;width:15px;height:15px;background:var(--blue-deep);color:#fff;font-size:6px;line-height:15px;text-align:center">01</div>
      <div class="abs tech" style="left:20px;top:-4px;font-size:4px">YOUR TITLE HERE</div>
      <p class="abs" style="left:20px;top:2px;width:104px;font-size:3.6px;line-height:4.8px">It has survived not only five centuries, but also the leap into electronic typesetting, in the 1960s with the release of Letraset sheets</p>
    </div>
    <div style="position:relative;height:33px">
      <div class="abs tech" style="left:0;top:0;width:15px;height:15px;background:#1567c4;color:#fff;font-size:6px;line-height:15px;text-align:center">02</div>
      <div class="abs tech" style="left:20px;top:-4px;font-size:4px">YOUR TITLE HERE</div>
      <p class="abs" style="left:20px;top:2px;width:104px;font-size:3.6px;line-height:4.8px">It has survived not only five centuries, but also the leap into electronic typesetting, in the 1960s with the release of Letraset sheets</p>
    </div>
    <div style="position:relative;height:35px">
      <div class="abs tech" style="left:0;top:0;width:15px;height:15px;background:var(--blue-mid);color:#fff;font-size:6px;line-height:15px;text-align:center">03</div>
      <div class="abs tech" style="left:20px;top:-4px;font-size:4px">YOUR TITLE HERE</div>
      <p class="abs" style="left:20px;top:2px;width:104px;font-size:3.6px;line-height:4.8px">It has survived not only five centuries, but also the leap into electronic typesetting, in the 1960s with the release of Letraset sheets</p>
    </div>
    <div style="position:relative;height:33px">
      <div class="abs tech" style="left:0;top:0;width:15px;height:15px;background:var(--blue-light);color:#fff;font-size:6px;line-height:15px;text-align:center">04</div>
      <div class="abs tech" style="left:20px;top:-4px;font-size:4px">YOUR TITLE HERE</div>
      <p class="abs" style="left:20px;top:2px;width:104px;font-size:3.6px;line-height:4.8px">It has survived not only five centuries, but also the leap into electronic typesetting, in the 1960s with the release of Letraset sheets</p>
    </div>
  </div>
</section>

<!-- Heading slide -->
<section class="slide" style="left:28px;top:953px;width:340px;height:190px;background:#fff">
  <div class="abs" style="left:0;top:0;width:136px;height:110px;background:var(--blue)"></div>
  <div class="photo" role="img" aria-label="Photo of rail tank cars at dusk" style="left:136px;top:0;width:204px;height:110px;background:linear-gradient(100deg,#4a4a3c,#8a6a45 30%,#3a342c 60%,#22241e)"></div>
  <div class="abs" style="left:24px;top:22px;width:168px;height:65px;background:#fff">
    <div class="tag" style="left:16px;top:12px;width:105px">HEADING HERE</div>
    <p class="lead" style="left:16px;top:32px;width:150px;font-size:4.8px;line-height:8.5px">Lorem ipsum is simply of the printing and typesetting industry printer took a galley.</p>
  </div>
  <div class="abs" style="left:25px;top:122px;width:90px">
    <svg class="icon" width="20" height="14" viewBox="0 0 20 14"><rect x="1" y="3" width="11" height="7"/><path d="M12 5h4l3 3v2h-7zM3 3V1h5v2"/><circle cx="5" cy="11.5" r="1.5"/><circle cx="15" cy="11.5" r="1.5"/></svg>
    <div class="tech" style="font-size:5.5px;margin-top:1px">HEADING HERE</div>
    <p style="font-size:3.9px;line-height:5.2px;margin-top:6px;text-align:justify">It to make a type specimen book. It has survived not only five centuries, but also the leap into It was popularised.</p>
  </div>
  <div class="abs" style="left:130px;top:118px;width:90px">
    <svg class="icon" width="14" height="18" viewBox="0 0 14 18"><rect x="1" y="2" width="12" height="12" rx="3"/><path d="M3 5h8v4H3zM4 1h6M3 17l2-3M11 17l-2-3"/></svg>
    <div class="tech" style="font-size:5.5px;margin-top:1px">HEADING HERE</div>
    <p style="font-size:3.9px;line-height:5.2px;margin-top:6px;text-align:justify">It to make a type specimen book. It has survived not only five centuries, but also the leap into It was popularised.</p>
  </div>
  <div class="abs" style="left:235px;top:122px;width:90px">
    <svg class="icon" width="18" height="14" viewBox="0 0 18 14"><rect x="1" y="1" width="10" height="9"/><path d="M11 4h3l3 3v3h-6z"/><circle cx="5" cy="11.5" r="1.5"/><circle cx="14" cy="11.5" r="1.5"/></svg>
    <div class="tech" style="font-size:5.5px;margin-top:1px">HEADING HERE</div>
    <p style="font-size:3.9px;line-height:5.2px;margin-top:6px;text-align:justify">It to make a type specimen book. It has survived not only five centuries, but also the leap into It was popularised.</p>
  </div>
</section>

<!-- Brand name -->
<div class="brand">
  <div style="font-size:27px;line-height:32px">FROSTLINE</div>
  <div style="font-size:9px;letter-spacing:5px;margin-top:6px">GROUND CONSULTING</div>
</div>

</body>
</html>
```